Flyer Valrun Take Away
Zielgruppe
Gastrobetrieb mit Afghanischer Küche. Hauptangebot: Reisgerichte, Teigtaschen und Korma (Currygerichte). ZG: Studenten/Schüller, Ladenbesitzer und Passanten, da es sehr Zentral liegt.
Aufgabenstellung
Flyer für die Neueröffnung

```html
<!DOCTYPE html>
<html lang="de">
<head>
<meta charset="utf-8">
<title>Valrun Take Away – Flyer Neueröffnung</title>
<link rel="stylesheet" href="https://fonts.googleapis.com/css2?family=Cabin:ital,wght@0,400;0,700;1,400&family=Staatliches&display=swap">
<style>
  :root {
    --page: #ffffff;
    --ink: #1f1f1f;
    --green: #6aa842;
    --pattern: #f2ddb8;
    --pattern-soft: #f7ead2;
    --frame: #3a3a3a;
    --price: #555555;
  }
  html, body { margin: 0; padding: 0; width: 1200px; height: 686px; overflow: hidden; background: var(--page); }
  body { position: relative; font-family: "Cabin", Arial, sans-serif; color: var(--ink); }

  .panel { position: absolute; top: 70px; width: 380px; height: 539px; border: 1px solid var(--frame); box-sizing: border-box; overflow: hidden; background: var(--page); }
  .panel--front { left: 205px; }
  .panel--menu { left: 620px; background: linear-gradient(135deg, var(--pattern), var(--pattern-soft) 50%, var(--pattern)); }

  .pattern-band { position: absolute; left: 0; width: 100%; background: linear-gradient(90deg, var(--pattern), var(--pattern-soft), var(--pattern)); }
  .pattern-band--top { top: 0; height: 30px; }
  .pattern-band--mid { top: 301px; height: 34px; }
  .pattern-band--bottom { top: 465px; height: 74px; }

  .food-photo { position: absolute; left: 0; top: 30px; width: 100%; height: 271px; background: radial-gradient(ellipse at 62% 58%, #c8642a 0%, #a9501f 28%, #5a3322 52%, #3a2620 80%); }

  .brand-box { position: absolute; left: 29px; top: 0; width: 106px; height: 146px; background: var(--page); display: flex; align-items: center; justify-content: center; text-align: center; }
  .brand-name { font-family: "Cabin", Arial, sans-serif; font-weight: 700; font-size: 17px; line-height: 1.15; color: var(--ink); }

  .rule { position: absolute; height: 2px; background: var(--green); }

  .headline { position: absolute; left: 0; width: 100%; top: 338px; text-align: center; font-family: "Staatliches", Impact, sans-serif; font-size: 27px; letter-spacing: 4px; color: var(--ink); }
  .info { position: absolute; font-size: 15.5px; line-height: 1; white-space: nowrap; color: var(--ink); }

  .menu-card { position: absolute; left: 1px; top: 38px; width: 340px; height: 463px; background: var(--page); }
  .menu-section { position: absolute; left: 28px; width: 305px; }
  .menu-title { font-family: "Staatliches", Impact, sans-serif; color: var(--green); font-size: 9px; letter-spacing: 1.6px; margin: 0 0 2px; line-height: 1.2; }
  .menu-item { font-size: 8px; line-height: 11.7px; margin: 0 0 11.7px; }
  .menu-item b { font-weight: 700; }
  .price { font-style: italic; color: var(--price); }
</style>
</head>
<body>

<section class="panel panel--front">
  <div class="pattern-band pattern-band--top"></div>
  <div class="food-photo" role="img" aria-label="Foto: afghanisches Curry in Metallschale mit Reis und Fladenbrot auf Holztisch"></div>
  <div class="brand-box"><span class="brand-name">Valrun<br>Take Away</span></div>
  <div class="pattern-band pattern-band--mid"></div>
  <div class="rule" style="left:0; top:331px; width:252px;"></div>
  <h1 class="headline" style="margin:0;">Neueröffnung! 02.11.15</h1>
  <p class="info" style="margin:0; left:63px; top:377px;">Lindenweg 21 // 8001 Zürich</p>
  <p class="info" style="margin:0; left:18px; top:397px;">Tel. +41 76 000 12 34 // www.valrun.ch</p>
  <p class="info" style="margin:0; left:43px; top:417px;">Montag – Samstag // 11:00 – 14:00 Mittags-Menü</p>
  <p class="info" style="margin:0; left:15px; top:436px;">18:00 – 22:00 Teigtaschen // Sonntag Ruhetag</p>
  <div class="rule" style="left:218px; top:458px; width:162px;"></div>
  <div class="rule" style="left:126px; top:465px; width:254px;"></div>
  <div class="pattern-band pattern-band--bottom"></div>
</section>

<section class="panel panel--menu">
  <div class="rule" style="left:0; top:30px; width:110px;"></div>
  <div class="rule" style="left:0; top:38px; width:298px;"></div>
  <div class="menu-card">
    <div class="menu-section" style="top:15px;">
      <h2 class="menu-title">Teigtaschen</h2>
      <p class="menu-item"><b>Mantu</b>: gedämpfte Teigtaschen gefüllt mit Rindshackfleisch und Zwiebeln, serviert an gelber Erbsensauce, Gemüse und Minze-Joghurt Sauce <span class="price">(Fr. 11.00)</span></p>
      <p class="menu-item"><b>Ashak</b>: poschierte Teigtaschen gefüllt mit Lauch serviert mit Hackfleisch- und Knoblauch- Minze-Joghurt Sauce <span class="price">(Fr. 12.00)</span></p>
      <p class="menu-item"><b>Boloni</b>: gebratene Teigtaschen gefüllt mit Kartoffeln oder Lauch, serviert mit Minze-Joghurt Sauce und Chakni (rassige Chili-Koriander Sauce) <span class="price">(Fr. 7.00)</span></p>
      <p class="menu-item"><b>Sambosa</b>: gebratene Teigtaschen gefüllt mit Kartoffel-Erbsen, serviert mit Knob-lauch-Minze-Joghurt Sauce dazu Salat und Chakni (rassige Chili-Koriander Sauce), 2 Stk. <span class="price">(Fr. 8.00)</span></p>
    </div>
    <div class="menu-section" style="top:193px;">
      <h2 class="menu-title">Mittags-Menü</h2>
      <p class="menu-item"><b>Shorba</b>: Traditionelle afghanische Suppe, Brotscheibe und ein Frucht <span class="price">(Fr. 11.00)</span></p>
      <p class="menu-item"><b>Korma</b>: Rassige Fleisch/Gemüse Curry zubereitet mit orientalischen Gewürzmischungen</p>
      <p class="menu-item"><b>Tarkori</b> : Pikant zubereitete Gemüse mit Tomaten-Sauce</p>
      <p class="menu-item"><b>Chalau / Palau:</b> Afghanische Festtags- und Nationalgericht aus Basmati-Reis <span class="price">(Fr. 14.50)</span></p>
    </div>
    <div class="menu-section" style="top:311px;">
      <h2 class="menu-title">Kabob</h2>
      <p class="menu-item"><b>Shami Kabob</b>: Hackfleischspiess serviert mit Salat nach afghanischer Art und frisch gebackenem Tandoori Brot <span class="price">(Fr. 9.00)</span></p>
    </div>
    <div class="menu-section" style="top:370px;">
      <h2 class="menu-title">Tee-Spezialität</h2>
      <p class="menu-item"><b>Shirr-Tschai</b>: Milch-Tee nach afghanischer Art mit Kardamom <span class="price">(Fr. 4.00)</span></p>
    </div>
    <div class="menu-section" style="top:417px;">
      <h2 class="menu-title">Süss-Gebäck</h2>
      <p class="menu-item"><b>Root</b> : Afghanisches Süssgebäck mit gemahlenen Mandeln, braunem Zucker und Schwarzkümmel <span class="price">(Fr. 4.00)</span></p>
    </div>
  </div>
  <div class="rule" style="left:198px; top:500px; width:182px;"></div>
</section>

</body>
</html>
```